Website redesign

We need a bold revamp of our website (http://www.brantocksparkworks.co.nz/)
which at the moment looks dated. We want a crisp, fresh and bold look. The background image behind web page can go. Open to complete new layout

Target Market(s)

Electrical contracting company- working in the domestic and commercial field

Coding

Coded - Design and coding required

Number of Pages Required

5+ page

Font styles to use
Sans Serif

Colors

Designer to choose colors to be used in the design.

```html
<!DOCTYPE html>
<html lang="en">
<head>
<meta charset="utf-8">
<title>Brantock Sparkworks – Electrical Installation &amp; Maintenance</title>
<link rel="stylesheet" href="https://fonts.googleapis.com/css2?family=Open+Sans:wght@400;600;700&family=Montserrat:wght@600;700&display=swap">
<style>
:root{
  --red:#e3262b;
  --navy:#1f2c52;
  --ink:#2a2f3d;
  --muted:#8a8f9c;
  --light:#f1f2f6;
  --line:#e2e4ea;
  --white:#ffffff;
}
*{box-sizing:border-box;margin:0;padding:0}
html,body{width:1200px;height:3084px;overflow:hidden}
body{font-family:"Open Sans",Arial,sans-serif;color:var(--ink);background:var(--white);font-size:12px;line-height:1.6}
h1,h2,h3,h4{font-family:"Montserrat","Open Sans",sans-serif}
.page{position:relative;width:1200px;height:3084px}

/* hero */
.hero{position:relative;height:560px;background:linear-gradient(180deg,#0c1838 0%,#23396b 45%,#4d6a9a 75%,#aab7c9 100%)}
.hero-photo{position:absolute;inset:0}
.nav{position:absolute;top:0;left:0;right:0;height:64px;display:flex;align-items:center;padding:0 40px}
.brand{display:flex;align-items:center;gap:8px;color:var(--white);font-weight:700;font-size:15px}
.brand-mark{width:18px;height:18px;background:var(--red)}
.menu{display:flex;gap:34px;margin-left:150px}
.menu a{color:var(--white);text-decoration:none;font-size:11px;font-weight:700;letter-spacing:.5px}
.nav-right{margin-left:auto;text-align:right;color:var(--white);font-size:10px}
.btn-quote{display:inline-block;margin-top:6px;background:var(--white);color:var(--navy);font-size:10px;font-weight:600;padding:5px 12px;border-radius:3px}

.intro{height:110px;text-align:center;padding-top:22px}
.intro h2{font-size:20px;font-weight:700;color:var(--navy);line-height:1.35;width:760px;margin:0 auto}
.intro p{color:var(--muted);font-size:11px;margin-top:8px}

.eyebrow{color:var(--red);font-size:11px}
.section-title{font-size:28px;font-weight:700;color:var(--navy);margin:2px 0 10px}
.section-lede{color:var(--muted);font-size:11px;width:360px}
.center{text-align:center}
.center .section-lede{margin:0 auto;width:420px}

/* services */
.services{background:var(--light);height:680px;padding:40px 40px 0}
.svc-panel{display:flex;margin-top:48px;gap:40px}
.svc-tabs{width:230px;list-style:none;padding-top:8px}
.svc-tabs li{display:flex;align-items:center;gap:12px;height:48px;padding-left:12px;font-size:11px}
.svc-tabs li.active{background:var(--white);box-shadow:0 2px 8px rgba(0,0,0,.06)}
.svc-thumb{width:28px;height:28px;border-radius:50%;background:linear-gradient(135deg,#5c6d8a,#b8c2d1)}
.svc-body{flex:1;background:var(--white);padding:34px 40px;height:450px}
.svc-body h3{font-size:20px;color:var(--navy);margin-bottom:14px}
.svc-body p{color:var(--muted);font-size:11px;margin-bottom:12px}
.more{color:var(--red);font-size:11px;font-weight:600}
.svc-gallery{display:flex;gap:26px;margin-top:14px}
.svc-gallery div{width:200px;height:110px}
.g1{background:linear-gradient(135deg,#cfd6e0,#7b8aa0)}
.g2{background:linear-gradient(135deg,#e7d6d4,#b2484a)}
.g3{background:linear-gradient(135deg,#c7c9cf,#6e7380)}

/* features */
.features{height:670px;padding-top:60px}
.feature-grid{display:grid;grid-template-columns:repeat(3,250px);column-gap:40px;row-gap:48px;width:830px;margin:60px auto 0}
.feature svg{width:26px;height:26px;margin-bottom:10px}
.feature h4{font-size:15px;color:var(--navy);margin-bottom:6px}
.feature p{color:var(--muted);font-size:11px}

/* testimonials */
.testimonials{background:var(--light);height:530px;padding-top:60px}
.quote-grid{display:grid;grid-template-columns:repeat(2,500px);column-gap:60px;row-gap:40px;width:1060px;margin:60px auto 0}
.quote{display:flex;gap:22px;align-items:flex-start}
.quote p{color:var(--muted);font-size:11px}
.quote cite{display:block;text-align:right;font-style:normal;font-size:11px;color:var(--ink);margin-top:6px}
.avatar{flex:none;width:60px;height:60px;border-radius:50%;background:linear-gradient(135deg,#c9ccd4,#6e7482)}
.quote.flip{flex-direction:row-reverse}
.quote.flip cite{text-align:left}

/* contact */
.contact{display:grid;grid-template-columns:330px 460px 300px;gap:40px;padding:40px 40px 0;height:360px}
.contact h4{font-size:15px;font-weight:600;color:var(--navy);margin-bottom:14px}
.field{border:1px solid var(--line);height:28px;font-size:10px;color:var(--muted);padding:6px 8px;background:var(--white)}
.row{display:flex;gap:8px;margin-bottom:8px}
.row .field{flex:1}
.field.wide{margin-bottom:8px}
.field.area{height:70px;margin-bottom:12px}
.btn-send{display:inline-block;background:var(--red);color:var(--white);font-size:10px;font-weight:700;padding:7px 16px;border-radius:2px}
.map{height:220px;background:linear-gradient(135deg,#d9e2ea,#b7c8d6)}
.info p{color:var(--muted);font-size:11px;margin-bottom:6px}
.info b{color:var(--ink);font-weight:600}
.social{display:flex;gap:10px;margin-top:8px}
.social span{width:24px;height:24px;border-radius:50%;background:var(--red)}

/* footer */
.footer{position:absolute;left:0;right:0;bottom:0;height:170px;border-top:3px solid var(--red);padding:0 40px}
.foot-top{display:flex;align-items:center;height:80px;border-bottom:1px solid var(--line)}
.foot-links{display:flex;gap:28px;font-size:11px;color:var(--ink)}
.foot-brand{margin-left:auto;display:flex;align-items:center;gap:8px;color:var(--red);font-weight:700;font-size:16px}
.foot-brand i{width:16px;height:16px;background:var(--red)}
.foot-bottom{display:flex;justify-content:space-between;padding-top:18px;font-size:10px;color:var(--muted)}
.foot-bottom nav{display:flex;gap:20px}
</style>
</head>
<body>
<div class="page">

<header class="hero">
  <div class="hero-photo" role="img" aria-label="Modern timber home lit up at dusk with large glowing windows"></div>
  <nav class="nav">
    <div class="brand"><span class="brand-mark"></span>Brantock</div>
    <div class="menu"><a href="#">OUR COMPANY</a><a href="#">SERVICES</a><a href="#">PROJECTS</a><a href="#">CONTACT US</a></div>
    <div class="nav-right">Call: 0800 274 466<br><span class="btn-quote">Request a Quote</span></div>
  </nav>
</header>

<section class="intro">
  <h2>Brantock Sparkworks is a leading electrical installation and maintenance company based in Wanganui, but servicing all New Zealand.</h2>
  <p>See some of our latest projects and hear why customers trust Brantock Sparkworks</p>
</section>

<section class="services">
  <div class="eyebrow">Services</div>
  <h2 class="section-title">What we do ?</h2>
  <p class="section-lede">We are a company specialised in quality electrical installations in private houses, apartments and commercial spaces.</p>
  <div class="svc-panel">
    <ul class="svc-tabs">
      <li class="active"><span class="svc-thumb" role="img" aria-label="Electrical installation photo"></span>Electrical Installations</li>
      <li><span class="svc-thumb" role="img" aria-label="Appliances photo"></span>Appliances</li>
      <li><span class="svc-thumb" role="img" aria-label="Alarm panel photo"></span>Alarms &amp; Security</li>
      <li><span class="svc-thumb" role="img" aria-label="Phone and TV photo"></span>Phone Data &amp; TV</li>
      <li><span class="svc-thumb" role="img" aria-label="Heat pump photo"></span>Heat Pumps &amp; Fire Smoke</li>
    </ul>
    <div class="svc-body">
      <h3>Electrical Installations</h3>
      <p>From new builds to renovations we plan, wire and certify every circuit in your home or business. Our licensed team works cleanly, on schedule and always to current New Zealand standards and safety codes.</p>
      <p>We install switchboards, lighting, power points and outdoor fittings, then test each job before handover so you can switch on with complete confidence and peace of mind for years.</p>
      <span class="more">Details »</span>
      <div class="svc-gallery">
        <div class="g1" role="img" aria-label="Electrician fitting a light switch"></div>
        <div class="g2" role="img" aria-label="Wiring inside a switchboard"></div>
        <div class="g3" role="img" aria-label="Close-up of cable connections"></div>
      </div>
    </div>
  </div>
</section>

<section class="features center">
  <div class="eyebrow">Features</div>
  <h2 class="section-title">Why choose us ?</h2>
  <p class="section-lede">We have many years of honest experience on projects for different clients. We make sure to provide high quality work.</p>
  <div class="feature-grid" style="text-align:left">
    <div class="feature">
      <svg viewBox="0 0 24 24" fill="none" stroke="#e3262b" stroke-width="2"><circle cx="12" cy="12" r="9"/><path d="M12 7v5l3 3"/></svg>
      <h4>Arrival on time</h4><p>We show up when we say we will and keep you updated through every stage of the job.</p>
    </div>
    <div class="feature">
      <svg viewBox="0 0 24 24" fill="none" stroke="#e3262b" stroke-width="2"><path d="M4 20l9-9M14 4l6 6-4 4-6-6zM4 4l6 6"/></svg>
      <h4>Professional equipment</h4><p>Modern, well kept tools let us work faster, safer and with precise, lasting results.</p>
    </div>
    <div class="feature">
      <svg viewBox="0 0 24 24" fill="none" stroke="#e3262b" stroke-width="2"><path d="M5 4h14v10l-7 6-7-6z"/><path d="M9 11l2 2 4-4"/></svg>
      <h4>Proposition of best solution</h4><p>We listen first, then suggest the smartest option for your budget and your space.</p>
    </div>
    <div class="feature">
      <svg viewBox="0 0 24 24" fill="none" stroke="#e3262b" stroke-width="2"><path d="M2 12s4-7 10-7 10 7 10 7-4 7-10 7S2 12 2 12z"/><circle cx="12" cy="12" r="3"/></svg>
      <h4>Great sense for detail</h4><p>Neat cabling, tidy finishes and careful testing are part of every single job.</p>
    </div>
    <div class="feature">
      <svg viewBox="0 0 24 24" fill="none" stroke="#e3262b" stroke-width="2"><rect x="4" y="7" width="16" height="12" rx="1"/><path d="M9 7V4h6v3"/></svg>
      <h4>Professional approach</h4><p>Clear quotes, friendly staff and respect for your home from start to finish.</p>
    </div>
    <div class="feature">
      <svg viewBox="0 0 24 24" fill="none" stroke="#e3262b" stroke-width="2"><path d="M6 3h9l4 4v14H6z"/><path d="M9 13l2 2 4-4"/></svg>
      <h4>Compliance of your plans</h4><p>Every installation is certified and matched exactly to your approved plans.</p>
    </div>
  </div>
</section>

<section class="testimonials center">
  <div class="eyebrow">Testimonials</div>
  <h2 class="section-title">What our Clients say ?</h2>
  <p class="section-lede">What our clients say about our services and how we helped so many homeowners from the area.</p>
  <div class="quote-grid" style="text-align:left">
    <div class="quote flip">
      <span class="avatar" role="img" aria-label="Client portrait"></span>
      <div><p>The team rewired our whole house in under a week. They were tidy, polite and explained every step. We would not hesitate to call them again for our next project.</p><cite>Rowan Teague, Operations Manager</cite></div>
    </div>
    <div class="quote">
      <span class="avatar" role="img" aria-label="Client portrait"></span>
      <div><p>Great communication from quote to finish. Our new lighting looks fantastic and the price matched the estimate exactly. Highly recommended to anyone renovating.</p><cite>Mirela Haskins, Creative Designer</cite></div>
    </div>
    <div class="quote flip">
      <span class="avatar" role="img" aria-label="Client portrait"></span>
      <div><p>They installed our alarm and heat pump on the same day. Friendly staff, clean work and a clear walkthrough of the system before they left our home.</p><cite>Odile Farrant, Manager</cite></div>
    </div>
    <div class="quote">
      <span class="avatar" role="img" aria-label="Client portrait"></span>
      <div><p>Fast response to an urgent fault at our office. The electrician found the problem quickly and had us back up and running within the hour. Superb service.</p><cite>Casper Wendt, Developer</cite></div>
    </div>
  </div>
</section>

<section class="contact">
  <div>
    <h4>Feel Free to Mail</h4>
    <div class="row"><div class="field">Name*</div><div class="field">Email*</div></div>
    <div class="field wide">Subject</div>
    <div class="field area">Write Your Message Here...</div>
    <span class="btn-send">SEND MESSAGE</span>
  </div>
  <div>
    <h4 style="text-align:center">Headquarters</h4>
    <div class="map" role="img" aria-label="Street map of Wanganui with office location pin"></div>
  </div>
  <div class="info">
    <h4>Contact Info</h4>
    <p>Get in touch for a quote, call us or drop by our office in Wanganui.</p>
    <p><b>Phone:</b> 0800 274 466</p>
    <p><b>Office:</b> 14 Harbour Rd, Wanganui</p>
    <p><b>Email:</b> hello@brantocksparkworks.co.nz</p>
    <h4 style="margin-top:14px">Follow Us</h4>
    <div class="social"><span></span><span></span><span></span><span></span><span></span></div>
  </div>
</section>

<footer class="footer">
  <div class="foot-top">
    <div class="foot-links"><span>Home</span><span>Help &amp; Contact</span><span>Services</span><span>Our Projects</span><span>Request a Quote</span></div>
    <div class="foot-brand"><i></i>Brantock</div>
  </div>
  <div class="foot-bottom">
    <nav><span>About</span><span>News</span><span>Gallery</span><span>Partners</span><span>Careers</span><span>Team</span></nav>
    <nav><span>© 2024 – 2025</span><span>Privacy</span><span>Legal</span><span>Sitemap</span></nav>
  </div>
</footer>

</div>
</body>
</html>
```